Anzeigengestaltung für Fliesenlegermeister
Zielgruppe
Ich bin ein Fliesenlegermeister und möchte mich selbstständig machen, ich saniere Bäder, Böden mit Fliesen, Fliesenspiegel und ich möchte eine Anzeige in den regionalen Zeitungen machen. Ich spreche alle Altersklassen mit Bädern für Sanierungen, Bodenfliesen und Neubauten an. Reparatur und Silikonarbeiten sowie Trockenbauarbeiten am eigenen Heim .
Aufgabenstellung
Ich möchte gern meine Kontaktdaten und die Farben vom Logo wieder finden,
als Beispiel habe ich meine aktuelle Visitenkarte beigefügt Dort finden sich die Kontaktdaten. Meine Arbeiten sind insbesondere :
Fliesenverlegung
Badsanierung
barrierefreie Bäder
Reparaturarbeiten
Silikonarbeiten
Trockenbau
Ob nun genau alle 6 Punkte in der Anzeige angezeigt werden soll bin ich mir nicht sicher oder ob nur 4 Beschreibungen reichen, damit es nicht zu viel wird.

```html
<!DOCTYPE html>
<html lang="de">
<head>
<meta charset="utf-8">
<title>Anzeige Fliesenlegermeister Jonas Brenner</title>
<link href="https://fonts.googleapis.com/css2?family=Lato:wght@400;700&display=swap" rel="stylesheet">
<style>
  :root {
    --brand-blue: #0b4594;
    --graphite: #3b3b3d;
    --paper: #ffffff;
    --backdrop: #e9e9eb;
    --ink: #2a2a2c;
  }
  * { box-sizing: border-box; margin: 0; padding: 0; }
  html, body { width: 1200px; height: 785px; overflow: hidden; }
  body {
    background: var(--backdrop);
    font-family: "Lato", Arial, sans-serif;
    display: flex; align-items: center; justify-content: center;
  }
  .ad {
    width: 620px; height: 745px;
    background: var(--paper);
    position: relative;
    box-shadow: 0 2px 10px rgba(0,0,0,0.08);
  }
  .brand {
    position: absolute; top: 52px; right: 56px;
    display: flex; align-items: center; gap: 16px;
  }
  .brand-square { width: 54px; height: 54px; background: var(--brand-blue); }
  .brand-divider { width: 3px; height: 68px; background: var(--graphite); }
  .brand-name {
    font-weight: 700; font-size: 38px; letter-spacing: 2px;
    color: var(--brand-blue); text-transform: uppercase; line-height: 1;
  }
  .brand-trade {
    font-size: 19px; letter-spacing: 3.2px; color: var(--graphite);
    text-transform: uppercase; margin-top: 6px;
  }
  .services {
    position: absolute; top: 168px; left: 40px; right: 40px; height: 372px;
    background: var(--brand-blue);
    list-style: none; padding: 38px 0 0 58px;
  }
  .services li {
    color: var(--paper); text-transform: uppercase;
    font-size: 33px; letter-spacing: 1px; line-height: 52px;
    position: relative; padding-left: 42px;
  }
  .services li::before {
    content: ""; position: absolute; left: 0; top: 14px;
    width: 17px; height: 17px; background: var(--paper);
  }
  .contact { position: absolute; top: 570px; left: 0; right: 0; list-style: none; }
  .contact li { display: flex; align-items: center; height: 52px; margin-bottom: 4px; }
  .contact-tab {
    width: 104px; height: 44px; background: var(--graphite);
    display: flex; align-items: center; justify-content: flex-end; padding-right: 20px;
  }
  .contact-tab svg { width: 22px; height: 22px; }
  .contact-text { margin-left: 22px; font-size: 22px; color: var(--ink); }
</style>
</head>
<body>
  <article class="ad">
    <header class="brand">
      <span class="brand-square"></span>
      <span class="brand-divider"></span>
      <div>
        <div class="brand-name">Jonas Brenner</div>
        <div class="brand-trade">Fliesenlegermeister</div>
      </div>
    </header>

    <ul class="services">
      <li>Fliesenverlegung</li>
      <li>Badsanierung</li>
      <li>Barrierefreie Bäder</li>
      <li>Reparaturarbeiten</li>
      <li>Silikonarbeiten</li>
      <li>Trockenbau</li>
    </ul>

    <ul class="contact">
      <li>
        <span class="contact-tab">
          <svg viewBox="0 0 24 24" aria-hidden="true"><path fill="#fff" d="M6.6 10.8a15 15 0 0 0 6.6 6.6l2.2-2.2a1 1 0 0 1 1-.25 11.4 11.4 0 0 0 3.6.57 1 1 0 0 1 1 1V20a1 1 0 0 1-1 1A17 17 0 0 1 3 4a1 1 0 0 1 1-1h3.5a1 1 0 0 1 1 1c0 1.25.2 2.45.57 3.57a1 1 0 0 1-.25 1z"/></svg>
        </span>
        <span class="contact-text">05421/7786120 Mobil 01608452391</span>
      </li>
      <li>
        <span class="contact-tab">
          <svg viewBox="0 0 24 24" aria-hidden="true"><rect x="2.5" y="5" width="19" height="14" fill="none" stroke="#fff" stroke-width="2"/><path d="M3 6l9 7 9-7" fill="none" stroke="#fff" stroke-width="2"/></svg>
        </span>
        <span class="contact-text">info@fliesenlegermeister-brenner.de</span>
      </li>
      <li>
        <span class="contact-tab">
          <svg viewBox="0 0 24 24" aria-hidden="true"><path fill="#fff" d="M12 2a7 7 0 0 0-7 7c0 5.2 7 13 7 13s7-7.8 7-13a7 7 0 0 0-7-7zm0 9.5A2.5 2.5 0 1 1 12 6.5a2.5 2.5 0 0 1 0 5z"/></svg>
        </span>
        <span class="contact-text">Lindenweg 7, 38100 Musterstadt</span>
      </li>
    </ul>
  </article>
</body>
</html>
```